female stress management consultant, doctor, Health & Well-being coach needs a wordpress theme

I am a Stress management consultant, General Practitioner and Health and Well-Being coach who is targeting mainly surgeries/hospitals and corporate business.
I have my own URL drhelgabrunsvik.com and the hosting.
I need a WordPress Website that is easy to maintain and edit to regularly change the content (copy/pictures/action buttons/banners).
I want my website to look professional and elegant for corporate businesses and managers to feel they can trust me and my expertise. At the same time, the website should have a warm and welcoming feel to it. It should feel uplifting and very positive.
I am open to colour suggestions, but please incorporate the following two colours: #F18877 and #D2BB7A. For fonts I prefer grey over black (like #777777).
The website needs to create an impression of "know like and trust".
The website should have a sign-up button for a newsletter, multiple contact buttons over the home page - to write an email to me, contact details top and bottom and the possibility to have a video on the home page top instead of a picture (Best would be that I can change from picture to video to picture in the future without needing a designer). A video that can run in the background with text laid over. A bit like on this website from Tessa Lindqvor: https://www.tessalindqvor.com.
I need 5 pages: Home, About, Services, Contact, free resources. I do NOT need an e-commerce or booking facility as I will neither sell nor let people book through my website. I don't need a blog either.
All the pages need to have a link to my other website (brightpathdaily.co.uk) and it needs to state that the linked website (brightpathdaily) is my website with a blog and for private customers.
Please use the photos I attached if possible. Me with the dogs for the "about" section.

Websites I like: https://www.rosalbkq.com, tessalindqvor.com, https://pennyholtzbrook.com (this site is too dark for my liking, but the layout has a simple navigation layout, the important buttons are right up at the side (LinkedIn/social media/CTA), is minimalistic - hence easy to find the important bits).

surgeries/doctor offices, hospitals, corporate business

Health and well-being

5+ page

Sans Serif

• see project description
• see project description

```html
<!DOCTYPE html>
<html lang="en">
<head>
<meta charset="utf-8">
<title>Dr. Helga Brunsvik – Health &amp; Well-Being</title>
<link href="https://fonts.googleapis.com/css2?family=Lato:ital,wght@0,400;0,700;0,900;1,400;1,700&family=Dancing+Script:wght@600&display=swap" rel="stylesheet">
<style>
:root{
  --coral:#F18877;
  --gold:#D2BB7A;
  --blue:#3F55B8;
  --grey:#777777;
  --slate:#808080;
  --ink:#2a2a2a;
  --text:#444444;
  --paper:#F3F1F1;
  --white:#ffffff;
}
*{margin:0;padding:0;box-sizing:border-box}
html,body{width:1200px;height:4166px;overflow:hidden}
body{position:relative;font-family:'Lato',sans-serif;color:var(--text);background:var(--white)}
.abs{position:absolute}
.btn{position:absolute;display:flex;align-items:center;justify-content:center;background:var(--coral);color:var(--white);font-weight:700;font-size:20px;box-shadow:4px 4px 0 rgba(0,0,0,.25);text-decoration:none}
.center{left:0;width:1200px;text-align:center}

/* top bar */
.topbar{top:0;left:0;width:1200px;height:55px;background:var(--gold)}
.social{position:absolute;display:flex;gap:18px}
.social span{display:block;width:18px;height:18px;border-radius:50%;background:currentColor}
.topbar .social{left:75px;top:18px;color:var(--white)}
.topbar .mail{position:absolute;right:75px;top:15px;color:var(--white);font-size:18px;display:flex;align-items:center;gap:12px}

/* hero */
.hero{top:55px;left:0;width:1200px;height:789px;background:linear-gradient(180deg,#8fb7d8 0%,#2f6fa6 22%,#1f5f92 35%,#c9a98a 55%,#b08a6a 75%,#7a5a44 100%)}
.brand{position:absolute;display:flex;align-items:center;gap:12px;font-size:34px;font-weight:400;letter-spacing:1px;white-space:nowrap}
.brand i{display:block;width:30px;height:30px;border-radius:50%;border:2px solid currentColor}
.nav{position:absolute;top:85px;right:73px;display:flex;align-items:center;gap:40px;font-size:15px;font-weight:700;color:var(--white);letter-spacing:.5px}
.nav .active{color:var(--coral)}
.nav .cta{background:var(--coral);padding:16px 20px;box-shadow:3px 3px 0 rgba(0,0,0,.2)}
.hero-script{top:350px;font-family:'Dancing Script',cursive;font-size:80px;color:var(--white)}
.hero-title{top:452px;font-size:66px;font-weight:900;color:var(--white);text-shadow:0 2px 8px rgba(0,0,0,.3)}
.ghost{position:absolute;display:flex;align-items:center;justify-content:center;gap:8px;border:3px solid var(--white);color:var(--white);font-weight:700;font-size:22px;background:rgba(0,0,0,.15)}

/* about */
.about{top:844px;left:0;width:1200px;height:720px;background:var(--paper)}
.about h2{position:absolute;left:75px;top:70px;font-size:50px;font-weight:900;color:var(--ink);line-height:48px}
.about .deg{position:absolute;left:75px;top:168px;font-size:30px;font-weight:700;color:var(--gold)}
.about .lead{position:absolute;left:75px;top:228px;width:560px;font-size:23px;font-weight:700;color:var(--coral);line-height:32px}
.about p{position:absolute;left:75px;top:332px;width:560px;font-size:16.5px;line-height:27px;color:var(--text)}
.portrait{position:absolute;left:626px;top:922px;width:500px;height:500px;border-radius:50%;background:radial-gradient(circle at 45% 40%,#c8b49a,#6f8a4c 60%,#4a6a35)}
.ring{position:absolute;border-radius:50%}

.section-title{font-size:52px;font-weight:900;color:var(--ink)}

/* cards */
.card{position:absolute;top:1779px;width:330px;height:402px;text-align:center;color:var(--white)}
.card.gold{left:75px;background:var(--gold)}
.card.blue{left:435px;background:var(--blue)}
.card.slate{left:797px;background:var(--slate)}
.card h3{margin-top:96px;font-size:28px;font-weight:900;line-height:33px}
.card p{margin:18px auto 0;width:290px;font-size:16px;line-height:27px}
.icon{position:absolute;top:-56px;left:110px;width:110px;height:110px;border-radius:50%;background:var(--coral);border:6px solid var(--white)}

/* testimonials */
.testis{top:2272px;left:0;width:1200px;height:621px;background:linear-gradient(180deg,#5a3b2a 0%,#7a4a30 35%,#a06038 65%,#4a3226 100%)}
.quote{position:absolute;top:2524px;width:490px;height:288px;background:var(--white);padding:26px 28px 0 28px}
.quote h4{font-size:28px;font-style:italic;font-weight:400;color:var(--ink);line-height:36px}
.quote p{margin-top:12px;font-size:16px;line-height:28px;color:var(--text)}
.quote .who{margin-top:10px;font-size:20px;color:var(--coral)}
.quote .role{font-size:13.5px;font-style:italic;color:var(--text)}
.qmark{position:absolute;left:-20px;top:18px;width:40px;height:40px;border-radius:50%;background:var(--coral);color:var(--white);font-size:40px;font-weight:900;line-height:56px;text-align:center}

/* blog band */
.band{top:2893px;left:0;width:1200px;height:357px;background:var(--blue)}
.band h2{position:absolute;top:64px;left:0;width:1200px;text-align:center;color:var(--white);font-size:54px;font-weight:900;line-height:64px}

/* revitalise */
.revive{top:3250px;left:0;width:1200px;height:620px;background:linear-gradient(180deg,#6e6e6a 0%,#727568 50%,#6a6c63 100%)}

/* footer */
.footer h5{position:absolute;top:3892px;font-size:22px;font-weight:900;color:var(--coral)}
.footer ul{position:absolute;top:3938px;list-style:none;font-size:16.5px;color:var(--text);line-height:38px}
</style>
</head>
<body>

<header class="abs topbar">
  <div class="social" aria-label="Social links"><span></span><span></span><span></span><span></span><span></span></div>
  <div class="mail">
    <svg width="20" height="14" viewBox="0 0 20 14"><rect x="1" y="1" width="18" height="12" fill="none" stroke="#fff" stroke-width="2"/><path d="M1 1 L10 8 L19 1" fill="none" stroke="#fff" stroke-width="2"/></svg>
    info@drhelgabrunsvik.com
  </div>
</header>

<section class="abs hero" role="img" aria-label="Background photo: woman with raised arms on a wooden stairway above a sunny beach and sea"></section>
<div class="brand" style="left:78px;top:82px;color:var(--white)"><i></i>Dr. Helga Brunsvik</div>
<nav class="nav">
  <span class="active">HOME</span><span>ABOUT</span><span>SERVICES</span><span>FREE RESOURCES</span><span class="cta">CONTACT</span>
</nav>
<div class="abs center hero-script">Live Your Best Life</div>
<div class="abs center hero-title">Happy &amp; Healthy &amp; Full Of Joy!</div>
<a class="btn" style="left:391px;top:575px;width:198px;height:56px;font-size:22px">Contact Us</a>
<div class="ghost" style="left:615px;top:575px;width:196px;height:56px">
  <svg width="20" height="20" viewBox="0 0 20 20"><circle cx="10" cy="10" r="8.5" fill="none" stroke="#fff" stroke-width="2"/><path d="M8 6 L14 10 L8 14Z" fill="#fff"/></svg>Play Video
</div>
<svg class="abs" style="left:562px;top:770px" width="76" height="24" viewBox="0 0 76 24">
  <path d="M26 12 H4 M11 5 L4 12 L11 19" stroke="#fff" stroke-width="3" fill="none"/>
  <path d="M50 12 H72 M65 5 L72 12 L65 19" stroke="#fff" stroke-width="3" fill="none"/>
</svg>

<section class="abs about">
  <h2>About<br>Dr. Helga Brunsvik</h2>
  <div class="deg">MD, PHD</div>
  <div class="lead">Unlock the Power of Joy and Well-Being:<br>Discover Simple Steps to Restore Your Happiness<br>and Health Today!</div>
  <p>With over 30 years of being a doctor, I've met countless people facing<br>ongoing health issues and struggles that couldn't be solved solely<br>through conventional medicine. That's why it's so important to<br>embrace a holistic approach in our quest for balance, shifting from<br>discomfort to vitality and contentment.</p>
</section>
<a class="btn" style="left:75px;top:1348px;width:195px;height:56px;font-size:19px">More About Me</a>
<div class="ring" style="left:620px;top:912px;width:518px;height:518px;border:2px solid var(--gold)"></div>
<div class="ring" style="left:614px;top:922px;width:516px;height:516px;border:2px solid var(--coral)"></div>
<div class="portrait" role="img" aria-label="Photo of the doctor smiling, crouching outdoors on grass with her two dogs"></div>

<svg class="abs" style="left:0;top:1440px" width="1200" height="180" viewBox="0 0 1200 180" preserveAspectRatio="none">
  <path d="M0 180 L0 170 C250 20 700 150 1200 10 L1200 180Z" fill="var(--gold)"/>
  <path d="M0 180 C280 50 700 180 1200 40 L1200 180Z" fill="#fff"/>
</svg>

<h2 class="abs center section-title" style="top:1626px">How I Help</h2>

<div class="card gold">
  <div class="icon" role="img" aria-label="Icon: workshop group at a table"></div>
  <h3>Stress Mastery<br>Workshops</h3>
  <p>Let's embark on a journey together to create a life you love living. As your trusted health coach and experienced doctor, I'll provide comprehensive support and guidance.</p>
</div>
<div class="card blue">
  <div class="icon" role="img" aria-label="Icon: speaker giving a talk"></div>
  <h3>Talks</h3>
  <p>Let's embark on a journey together to create a life you love living. As your trusted health coach and experienced doctor, I'll provide comprehensive support and guidance.</p>
</div>
<div class="card slate">
  <div class="icon" role="img" aria-label="Icon: coach at a board with a group"></div>
  <h3>Coaching</h3>
  <p>Let's embark on a journey together to create a life you love living. As your trusted health coach and experienced doctor, I'll provide comprehensive support and guidance.</p>
</div>
<a class="btn" style="left:143px;top:2154px;width:195px;height:56px;font-size:19px">Read More</a>
<a class="btn" style="left:503px;top:2154px;width:195px;height:56px;font-size:19px">Read More</a>
<a class="btn" style="left:865px;top:2154px;width:195px;height:56px;font-size:19px">Read More</a>

<section class="abs testis" role="img" aria-label="Background photo: silhouette at sunset with birds in a warm sky"></section>
<svg class="abs" style="left:0;top:2270px" width="1200" height="170" viewBox="0 0 1200 170" preserveAspectRatio="none">
  <path d="M0 0 H1200 V0 C900 150 500 30 0 110Z" fill="var(--gold)"/>
  <path d="M0 0 H1200 V0 C880 110 480 10 0 90Z" fill="#fff"/>
</svg>
<h2 class="abs section-title" style="left:77px;top:2436px;color:var(--white)">Testimonials</h2>
<svg class="abs" style="left:1042px;top:2450px" width="88" height="36" viewBox="0 0 88 36">
  <path d="M32 18 H6 M16 7 L5 18 L16 29" stroke="#fff" stroke-width="4" fill="none"/>
  <path d="M56 18 H82 M72 7 L83 18 L72 29" stroke="#fff" stroke-width="4" fill="none"/>
</svg>
<div class="quote" style="left:97px">
  <div class="qmark">"</div>
  <h4>"I feel more positive and stopped procrastination."</h4>
  <p>" Working with Dr Helga has helped me stay more positive and helped me to stop procrastination. I feel more connected to my True Self - the True Self we loose as we progress through life.."</p>
  <div class="who">Maren Ashcroft</div>
  <div class="role">Counsellor, Hypnotherapist, Reiki master, Reflexologist</div>
</div>
<div class="quote" style="left:637px">
  <div class="qmark">"</div>
  <h4>"I feel more positive and stopped procrastination."</h4>
  <p>" Working with Dr Helga has helped me stay more positive and helped me to stop procrastination. I feel more connected to my True Self - the True Self we loose as we progress through life.."</p>
  <div class="who">Maren Ashcroft</div>
  <div class="role">Counsellor, Hypnotherapist, Reiki master, Reflexologist</div>
</div>

<section class="abs band">
  <h2>For Blog &amp;<br>For Private Customers</h2>
</section>
<a class="btn" style="left:446px;top:3118px;width:308px;height:56px;font-size:22px">Visit BrightPath Daily Now</a>

<section class="abs revive" role="img" aria-label="Background photo: woman relaxing in a green meadow, muted overlay"></section>
<h2 class="abs center" style="top:3350px;color:var(--white);font-size:54px;font-weight:900">Revitalise Your Life with Ease</h2>
<h3 class="abs center" style="top:3408px;color:var(--coral);font-size:36px;font-weight:900">Master the Art of Self-Care in Simple, yet Powerful Ways!</h3>
<p class="abs" style="top:3476px;left:75px;width:1050px;color:var(--white);font-size:18.5px;line-height:34px;text-align:center">Feeling exhausted, overwhelmed, and constantly drained of energy? It's time to break free from the burdens that weigh you down. Have you experienced unexplained irritability, tearfulness, or a persistent feeling of being down? You know deep down that this isn't the real you. It's time to reclaim your vitality and joy.</p>
<a class="btn" style="left:438px;top:3606px;width:324px;height:56px;font-size:22px">Start Your Exciting Future</a>

<svg class="abs" style="left:0;top:3740px" width="1200" height="140" viewBox="0 0 1200 140" preserveAspectRatio="none">
  <path d="M0 140 V120 C300 10 700 130 1200 0 V140Z" fill="var(--gold)"/>
  <path d="M0 140 C320 40 720 150 1200 30 V140Z" fill="#fff"/>
</svg>

<footer class="footer">
  <div class="brand" style="left:75px;top:3966px;font-size:28px;color:var(--coral)"><i style="width:26px;height:26px"></i>Dr. Helga Brunsvik</div>
  <div class="abs" style="left:75px;top:4040px;font-size:14.5px;line-height:26px;color:var(--text)">Copyright © 2023 Company Name<br>All Rights Reserved.</div>

  <h5 style="left:435px">Site Map</h5>
  <ul style="left:435px"><li>Home</li><li>About</li><li>Services</li><li>Free Resources</li><li>Contact</li></ul>
  <h5 style="left:651px">Legal</h5>
  <ul style="left:651px"><li>Disclaimer</li><li>Privacy Policy</li></ul>
  <h5 style="left:870px">Contact</h5>
  <div class="abs" style="left:870px;top:3947px;font-size:16.5px;display:flex;align-items:center;gap:14px;color:var(--text)">
    <svg width="18" height="13" viewBox="0 0 20 14"><rect x="1" y="1" width="18" height="12" fill="none" stroke="var(--coral)" stroke-width="2"/><path d="M1 1 L10 8 L19 1" fill="none" stroke="var(--coral)" stroke-width="2"/></svg>
    info@drhelgabrunsvik.com
  </div>
  <a class="btn" style="left:870px;top:3983px;width:256px;height:52px;font-size:16px;letter-spacing:.5px">NEWSLETTER SIGN UP</a>
  <div class="social" style="left:870px;top:4074px;color:#444;gap:22px" aria-label="Social links"><span></span><span></span><span></span><span></span><span></span></div>
</footer>

</body>
</html>
```